www.brightlingua.net -- International Language school needs a Wordpress Design

NOTE: This is for a complete WordPress website with coding (Design/develop)

We are a small, private English language school in business for 15 years. Our students come from around the world to study English at our centre in Toronto, Canada. Most of our students are in their 20's and come to study English with us for periods of 1-6 months before returning home to complete their post-secondary education or pursue their careers.

We are looking for a talented web designer to redevelop our sadly outdated website (www.brightlingua.net) to bring a fresh look with vastly increased functionality and web traffic.

Target Market(s)

-20s and 30s; mostly upper-middle class, educated
-from non-English speaking countries, but often have some English background
-looking to improve their English (mostly speaking) skills at our school like ours and experience living in a new country (like exchange students)

Industry/Entity Type

Education

Font styles to use
Sans Serif

Requirements
Must have
• - page listing our programs
- page with our fees and starting dates
- application form
- page showing why BRIGHT (us)?
- page with accommodation options
* responsive design
Nice to have
• examples of other websites in our industry I like:

http://www.halvorsenlang.com/
http://www.pqlearning.com/en
http://en.rtz.ca/
http://www.marstowe-academy.ac.uk/

```html
<!DOCTYPE html>
<html lang="en">
<head>
<meta charset="utf-8">
<title>Bright English School</title>
<link href="https://fonts.googleapis.com/css2?family=Open+Sans:wght@300;400;600;700&family=Comfortaa:wght@400&display=swap" rel="stylesheet">
<style>
:root{
  --orange:#ef8a05;
  --orange-dark:#d97800;
  --green:#1d8c69;
  --green-light:#2aa57d;
  --charcoal:#2d2d2d;
  --topbar:#3b3b3b;
  --ink:#333;
  --muted:#777;
  --line:#dedede;
  --footer:#f1f1f1;
  --white:#fff;
}
*{box-sizing:border-box;margin:0;padding:0}
html,body{width:1200px;height:2345px;overflow:hidden}
body{font-family:"Open Sans",Arial,sans-serif;color:var(--ink);background:var(--white);position:relative}
a{color:inherit;text-decoration:none}

.topbar{height:34px;background:var(--topbar);color:#ddd;font-size:11px;display:flex;align-items:center;padding:0 68px}
.topbar .contact{display:flex;gap:26px;align-items:center}
.topbar .contact span{display:flex;align-items:center;gap:6px}
.topbar .quick{display:flex;gap:18px;margin-left:34px}
.topbar .social{display:flex;gap:8px;margin-left:auto}
.topbar .social i{width:21px;height:21px;border:1px solid var(--orange);border-radius:50%;display:block}

.header{position:absolute;top:34px;left:0;width:1200px;height:100px;background:linear-gradient(var(--orange),var(--orange-dark));display:flex;align-items:center;padding:0 68px;z-index:2}
.brand{display:flex;align-items:center;gap:10px;font-size:36px;font-weight:700;color:var(--charcoal)}
.brand .dot{width:30px;height:30px;border-radius:50%;background:var(--charcoal)}
.nav{margin-left:auto;display:flex;gap:18px;font-size:13px;color:var(--white)}
.nav a.active{color:var(--charcoal);border-bottom:2px solid var(--charcoal);padding-bottom:3px}

.hero{position:absolute;top:34px;left:0;width:1200px;height:460px;display:flex}
.hero .photo{width:828px;background:linear-gradient(180deg,#e8e4df 20%,#f6f4f2 75%,#fff)}
.hero .tagline{flex:1;background:var(--green);display:flex;align-items:center;justify-content:center;text-align:center;font-family:"Comfortaa",sans-serif;color:var(--white);font-size:23px;line-height:1.15;letter-spacing:1px;padding-top:92px}

.programs{position:absolute;top:494px;left:0;width:1200px;height:144px;background:var(--charcoal);display:flex;padding:8px 42px 0 67px}
.programs .item{width:266px;text-align:center;color:var(--white);font-weight:300;font-size:32px;line-height:1.1;padding-top:4px}
.programs .item small{display:block;font-size:12px;font-weight:600;margin-top:10px}
.programs .item.current{background:var(--orange);width:242px;height:101px;margin-right:36px}
.programs .item.current span{display:block}

.intro{position:absolute;top:651px;left:0;width:1200px;height:465px;border-top:1px solid var(--line)}
.about{position:absolute;left:67px;top:35px;width:687px}
.about h2{font-size:20px;font-weight:400;margin-bottom:9px}
.tabs{border:1px solid var(--line);border-radius:3px;height:377px}
.tabs ul{list-style:none;display:flex;border-bottom:1px solid var(--line);font-size:13px;height:34px;align-items:center}
.tabs li{padding:0 12px;border-right:1px solid var(--line);line-height:34px}
.tabs li.on{color:var(--orange)}
.tabs .pics{display:flex;margin:22px 18px 0;height:182px}
.tabs .pics div:first-child{width:392px;background:linear-gradient(135deg,#c9a88a,#6e6a74)}
.tabs .pics div:last-child{flex:1;background:linear-gradient(135deg,#bcbcbc,#5d5b63)}
.tabs p{margin:6px 18px;font-size:11.5px;color:var(--muted);line-height:1.55}
.tabs p b{color:#555}

.enquiry{position:absolute;left:809px;top:35px;width:334px}
.enquiry h2{font-size:20px;font-weight:400;margin-bottom:9px}
.fields{border:1px solid var(--line);border-radius:3px}
.fields div{height:36px;border-bottom:1px solid var(--line);font-size:12px;color:#888;line-height:36px;padding:0 10px}
.fields div:last-child{border-bottom:0}
.message{margin-top:14px;border:1px solid var(--line);border-radius:3px;height:135px;font-size:12px;color:#888;padding:8px 10px}
.send{display:flex;align-items:center;margin-top:16px}
.send span{background:var(--orange);color:var(--white);font-size:12px;padding:7px 10px;border-radius:3px}
.send em{margin-left:auto;font-style:normal;color:var(--orange);font-size:11px}

.corner{position:absolute;top:1137px;left:0;width:1200px;height:316px;background:var(--green);color:var(--white);text-align:center}
.corner h2{font-size:40px;font-weight:400;padding-top:26px}
.corner .cols{display:flex;margin:20px 52px 0}
.corner .col{flex:1;border-right:1px solid rgba(255,255,255,.45);height:136px;padding:0 22px}
.corner .col:last-child{border-right:0}
.corner h3{font-size:19px;font-weight:400;color:#1b1b1b;margin:4px 0 6px}
.corner p{font-size:12.5px;line-height:1.6}
.corner svg{width:56px;height:56px}
.totop{position:absolute;right:18px;top:50px;width:28px;height:28px;border-radius:50%;background:var(--green-light)}

.voices{position:absolute;top:1453px;left:0;width:1200px;height:532px;background:var(--charcoal);color:var(--white);text-align:center}
.voices h2{font-size:29px;font-weight:400;padding-top:36px}
.quote{margin:18px 20px 0 32px;border:1px solid #888;border-radius:3px;height:160px;padding:18px 30px;font-size:17px;font-weight:600;line-height:1.45;position:relative}
.quote .who{position:absolute;left:16px;bottom:18px;display:flex;align-items:center;gap:12px;font-size:11px;color:#666;font-weight:400}
.quote .who i{width:38px;height:38px;border-radius:50%;background:#d8c6a7;display:block}
.tab-marker{position:absolute;left:0;top:210px;width:12px;height:60px;background:var(--orange)}
.pager{display:block;font-size:12px;color:#999;letter-spacing:3px;line-height:12px;margin-top:10px}
.voices h3{font-size:29px;font-weight:400;margin-top:0}
.strip{display:flex;gap:18px;margin:16px 0 0 32px}
.strip div{width:240px;height:170px;flex:none}
.strip div:nth-child(1){background:linear-gradient(#b8c6d0,#e3e8ea)}
.strip div:nth-child(2){background:linear-gradient(#6b5a4a,#d9cdb8)}
.strip div:nth-child(3){background:linear-gradient(#7a7a7a,#3c3a3a)}
.strip div:nth-child(4){background:linear-gradient(#a48c74,#e8dfd2)}
.strip div:nth-child(5){width:112px;background:linear-gradient(#6c5e58,#c8b8a8)}
.arrow{position:absolute;right:22px;top:385px;width:20px;height:46px;background:var(--orange);border-radius:3px}

.footer{position:absolute;top:1985px;left:0;width:1200px;height:295px;background:var(--footer)}
.footer .cols{display:flex;padding:72px 0 0 121px}
.footer .col{width:250px}
.footer h4{font-size:14px;font-weight:400;color:#444;margin-bottom:16px}
.footer li{list-style:none;font-size:11.5px;color:#888;line-height:17px}
.post{display:flex;gap:14px;font-size:11px;color:#888}
.post i{width:50px;height:50px;border-radius:50%;border:1px solid #ccc;display:block;flex:none}
.post b{display:block;font-size:10px;color:#444;font-weight:400;margin-top:3px}
.thumbs{display:grid;grid-template-columns:repeat(4,53px);gap:2px}
.thumbs div{height:53px;background:linear-gradient(135deg,#8a6a5a,#4f6a4a)}
.bottom{position:absolute;top:2280px;left:0;width:1200px;height:65px;display:flex;align-items:center;padding:0 123px;border-top:1px solid var(--line)}
.bottom .brand{font-size:30px}
.bottom .brand .dot{width:24px;height:24px}
.bottom small{margin-left:30px;font-size:10px;color:#888}
.bottom .up{position:absolute;right:8px;bottom:-8px;width:30px;height:30px;border-radius:50%;background:#e9b675}
</style>
</head>
<body>

<div class="topbar">
  <div class="contact">
    <span>&#9679; 415 Larkfield Avenue, Suite 12 Toronto, Ontario M2K 5R8 Canada</span>
    <span>&#9742; +1-416-555-0182</span>
    <span>&#9993; info@brightlingua.net</span>
    <span>&#9719; 9am -4pm</span>
  </div>
  <div class="quick"><a>News</a><a>Agent</a><a>Download</a></div>
  <div class="social"><i></i><i></i><i></i><i></i><i></i></div>
</div>

<div class="hero">
  <div class="photo" role="img" aria-label="Group of smiling young international students"></div>
  <div class="tagline">make friends around<br>the world</div>
</div>

<header class="header">
  <div class="brand"><span class="dot"></span>bright</div>
  <nav class="nav">
    <a class="active">HOME</a><a>OUR SCHOOL &#711;</a><a>PROGRAMS &#711;</a><a>FEES &amp; DATES &#711;</a><a>ACCOMMODATION &#711;</a><a>STUDENTS CORNER &#711;</a>
  </nav>
</header>

<section class="programs">
  <div class="item current"><span>ENGLISH<br>COURSES</span><small>find our our all programs</small></div>
  <div class="item">Full-Time<br>Programs<small>Intensive Focus</small></div>
  <div class="item">Bright Junior<br>Programs<small>Parent &amp; Child</small></div>
  <div class="item">Special<br>Programs<small>University Bridge</small></div>
</section>

<section class="intro">
  <div class="about">
    <h2>Learn English from expert. Join Bright today</h2>
    <div class="tabs">
      <ul><li class="on">About us</li><li>Why Bright ?</li><li>Our Features</li><li>F A Q</li><li>Apply Online</li></ul>
      <div class="pics">
        <div role="img" aria-label="Students studying together around a classroom table"></div>
        <div role="img" aria-label="Students smiling in a school lounge"></div>
      </div>
      <p><b>Lorem Ipsum</b> is simply dummy text of the printing and typesetting industry. Lorem Ipsum has been the industry's standard dummy text ever since the 1500s, when an unknown printer took a galley of type and scrambled it to make a type specimen book. It has survived not only five centuries, but also the leap into electronic typesetting, remaining essentially unchanged. It was popularised in the 1960s with the release of Pressleaf sheets containing Lorem Ipsum passages, and more recently with desktop publishing software like Folio PageCraft including versions of Lorem Ipsum.</p>
    </div>
  </div>
  <form class="enquiry">
    <h2>Get in touch with Bright</h2>
    <div class="fields"><div>Name *</div><div>E-mail *</div><div>Telephone</div><div>Country</div></div>
    <div class="message">Message *</div>
    <div class="send"><span>Send message</span><em>clear &#8855;</em></div>
  </form>
</section>

<section class="corner">
  <h2>Student Corner</h2>
  <span class="totop"></span>
  <div class="cols">
    <div class="col">
      <svg viewBox="0 0 56 56"><path d="M8 22h10l14-9v30l-14-9H8z" fill="var(--orange)"/><path d="M38 20q5 8 0 16M43 15q9 13 0 26" stroke="var(--orange)" stroke-width="3" fill="none"/></svg>
      <h3>News &amp; Events</h3>
      <p>simply dummy text of the printing and typesetting industry. Lorem Ipsum has been the industry's standard dummy text ever since the 1500s,</p>
    </div>
    <div class="col">
      <svg viewBox="0 0 56 56"><path d="M16 8h28v36H16q-4 0-4 4V12q0-4 4-4z" fill="var(--orange)"/><path d="M12 48q0-4 4-4h28v4z" fill="#f6b04a"/><path d="M20 16h18M20 22h18" stroke="var(--green)" stroke-width="2"/></svg>
      <h3>Lessons</h3>
      <p>simply dummy text of the printing and typesetting industry. Lorem Ipsum has been the industry's standard dummy text ever since the 1500s,</p>
    </div>
    <div class="col">
      <svg viewBox="0 0 56 56"><rect x="6" y="14" width="44" height="32" rx="4" fill="var(--orange)"/><rect x="20" y="9" width="16" height="7" fill="var(--orange)"/><circle cx="28" cy="30" r="9" fill="var(--green)"/><circle cx="28" cy="30" r="5" fill="var(--orange)"/></svg>
      <h3>Photo Gallery</h3>
      <p>simply dummy text of the printing and typesetting industry. Lorem Ipsum has been the industry's standard dummy text ever since the 1500s,</p>
    </div>
    <div class="col">
      <svg viewBox="0 0 56 56"><rect x="8" y="26" width="9" height="22" fill="var(--orange)"/><path d="M20 26l8-16q5 0 4 7l-2 7h13q4 1 3 5l-4 16q-1 3-4 3H20z" fill="var(--orange)"/></svg>
      <h3>Meet our students</h3>
      <p>simply dummy text of the printing and typesetting industry. Lorem Ipsum has been the industry's standard dummy text ever since the 1500s,</p>
    </div>
  </div>
</section>

<section class="voices">
  <h2>What our students says about Bright English School</h2>
  <span class="tab-marker"></span>
  <div class="quote">
    Lorem Ipsum is simply dummy text of the printing and typesetting industry. Lorem Ipsum has been the industry's standard dummy text ever since the 1500s, when an unknown printer took a galley of type and scrambled it to make a type specimen book. It has survived not only five centuries, but also the leap into electronic typesetting, remaining essentially unchanged.
    <div class="who"><i role="img" aria-label="Student portrait"></i>Maria Lopez – Brazil</div>
  </div>
  <span class="pager">&middot;&middot;&middot;</span>
  <h3>Students Gallery</h3>
  <div class="strip">
    <div role="img" aria-label="Students ice skating outdoors"></div>
    <div role="img" aria-label="Students laughing at a dinner table"></div>
    <div role="img" aria-label="Students posing at a holiday party"></div>
    <div role="img" aria-label="Students decorating a gingerbread house"></div>
    <div role="img" aria-label="Students at a celebration"></div>
  </div>
  <span class="arrow"></span>
</section>

<footer class="footer">
  <div class="cols">
    <div class="col">
      <h4>KNOWLEDGEBASE</h4>
      <ul><li>Tips &amp; Tricks</li><li>Downloads</li><li>Articles and Magazines</li><li>Learn from the beginning</li><li>Tips &amp; Tricks</li><li>Downloads</li><li>Articles and Magazines</li><li>Learn from the beginning</li></ul>
    </div>
    <div class="col">
      <h4>NEWS &amp; BLOGS</h4>
      <div class="post"><i></i><span>Hello world!<b>February 7, 2015</b></span></div>
    </div>
    <div class="col">
      <h4>GALLERY</h4>
      <div class="thumbs" role="img" aria-label="Thumbnail photos of school events">
        <div></div><div></div><div></div><div></div><div></div><div></div>
      </div>
    </div>
    <div class="col">
      <h4>HELP DESK</h4>
      <ul><li>Student Forum</li><li>Course Enquiry</li><li>Classes and Time</li><li>Fees details</li><li>Apply online</li></ul>
    </div>
  </div>
</footer>

<div class="bottom">
  <div class="brand"><span class="dot"></span>bright</div>
  <small>Powered By : northpixel</small>
  <span class="up"></span>
</div>

</body>
</html>
```